Maple Crest Schools | brand new stationery!

We need stationery design with our new logo! Our company updated it's name and image and we like to incorporate the new one on our stationery, business cards and email signature. We are looking for fresh, new ideas!
Industry: Childcare, Elementary and Middle School
Company Name: Maple Crest Schools
Tagline: Bright Futures Start Here
Main colors: Blue, white and a little yellow
Star shape is something new for us! Do you see a way to incorporate it as a design element?

```html
<!DOCTYPE html>
<html lang="en">
<head>
<meta charset="utf-8">
<title>Maple Crest Schools – Business Card</title>
<link href="https://fonts.googleapis.com/css2?family=Josefin+Sans:wght@600&family=Poppins:wght@400;600&display=swap" rel="stylesheet">
<style>
  :root {
    --navy: #041a6e;
    --white: #ffffff;
    --yellow: #fbbf10;
    --ink: #231f20;
    --backdrop: #b4b4b4;
  }
  * { margin: 0; padding: 0; box-sizing: border-box; }
  html, body { width: 1200px; height: 1200px; overflow: hidden; }
  body {
    background: var(--backdrop);
    font-family: "Poppins", sans-serif;
    position: relative;
  }
  .card {
    position: absolute;
    left: 262px;
    width: 686px;
    height: 392px;
    border-radius: 22px;
    overflow: hidden;
    background: var(--navy);
  }
  .card--front { top: 165px; }
  .card--back { top: 653px; }
  .card__shape { position: absolute; inset: 0; }

  .contact { position: absolute; left: 28px; top: 100px; color: var(--white); }
  .contact__name {
    font-family: "Josefin Sans", sans-serif;
    font-weight: 600;
    font-size: 28px;
    letter-spacing: 0.5px;
    line-height: 1;
  }
  .contact__role { color: var(--yellow); font-size: 15px; margin-top: 2px; }
  .contact__list { list-style: none; margin-top: 16px; font-size: 15px; line-height: 19.5px; }
  .contact__item { display: flex; align-items: flex-start; }
  .contact__item + .contact__item { margin-top: 0; }
  .contact__item--gap { margin-top: 7px !important; }
  .contact__icon { width: 12px; height: 12px; margin: 4px 12px 0 2px; flex: none; fill: var(--yellow); }

  .brand { position: absolute; left: 390px; top: 120px; width: 270px; text-align: center; }
  .brand__dot { width: 54px; height: 54px; border-radius: 50%; background: var(--navy); margin: 0 auto 14px; }
  .brand__name {
    color: var(--ink);
    font-weight: 600;
    font-size: 34px;
    line-height: 38px;
  }

  .back-brand {
    position: absolute; left: 0; right: 0; top: 120px;
    text-align: center; color: var(--white);
    font-weight: 600; font-size: 52px; line-height: 58px;
  }
  .back-url {
    position: absolute; left: 0; right: 0; top: 337px;
    text-align: center; color: var(--white);
    font-size: 15px; letter-spacing: 3.6px;
  }
</style>
</head>
<body>

<section class="card card--front">
  <svg class="card__shape" viewBox="0 0 686 392" aria-hidden="true">
    <path d="M466 0 H686 V392 H468 L278 203 Q274 197 278 191 Z" fill="var(--white)"/>
    <polygon points="313,175 318.5,186.5 331,188 321.5,196.5 324,209 313,202.5 302,209 304.5,196.5 295,188 307.5,186.5" fill="var(--yellow)"/>
  </svg>

  <div class="contact">
    <h1 class="contact__name">DANIEL HAYES</h1>
    <p class="contact__role">President</p>
    <ul class="contact__list">
      <li class="contact__item">
        <svg class="contact__icon" viewBox="0 0 12 12"><path d="M6 0a4.3 4.3 0 0 0-4.3 4.3C1.7 7.5 6 12 6 12s4.3-4.5 4.3-7.7A4.3 4.3 0 0 0 6 0zm0 6a1.7 1.7 0 1 1 0-3.4A1.7 1.7 0 0 1 6 6z"/></svg>
        <span>2140 Willow Bend Road<br>Juneau, Alaska 34812</span>
      </li>
      <li class="contact__item contact__item--gap">
        <svg class="contact__icon" viewBox="0 0 12 12"><path d="M2.4 0.5l2 2.3-1 1.4a7 7 0 0 0 4.4 4.4l1.4-1 2.3 2-1.2 1.9C5.6 11.7.3 6.4.5 1.7z"/></svg>
        <span>555-214-7730</span>
      </li>
      <li class="contact__item">
        <svg class="contact__icon" viewBox="0 0 12 12"><path d="M3 0h6a1 1 0 0 1 1 1v10a1 1 0 0 1-1 1H3a1 1 0 0 1-1-1V1a1 1 0 0 1 1-1zm.5 1.5v8h5v-8z"/></svg>
        <span>555-610-4192</span>
      </li>
      <li class="contact__item">
        <svg class="contact__icon" viewBox="0 0 12 12"><path d="M3 0h6v4H3zM0 5h12v5H0zm2 6h8v1H2z"/></svg>
        <span>555-388-2047</span>
      </li>
      <li class="contact__item">
        <svg class="contact__icon" viewBox="0 0 12 12"><path d="M0 2h12v8H0zm1 1l5 3.5L11 3z" fill-rule="evenodd"/></svg>
        <span>info@maplecrestschools.com</span>
      </li>
      <li class="contact__item">
        <svg class="contact__icon" viewBox="0 0 12 12"><circle cx="6" cy="6" r="6"/><path d="M3 3.5h3l1 2-2 1 .5 3L4 7 2.5 5z" fill="var(--navy)"/></svg>
        <span>maplecrestschools.com</span>
      </li>
    </ul>
  </div>

  <div class="brand">
    <div class="brand__dot"></div>
    <p class="brand__name">Maple Crest<br>Schools</p>
  </div>
</section>

<section class="card card--back">
  <p class="back-brand">Maple Crest<br>Schools</p>
  <p class="back-url">WWW.MAPLECRESTSCHOOLS.COM</p>
</section>

</body>
</html>
```